BrightFern Life Insurance Web Design Project

We need a beautiful and simple website design to better explain our life insurance business, products and why people need life insurance.
We want the site to stand out as being simple and compelling.
As we are an old "friendly society" that has been in Australia for 130 years, we want to stand for trust, simplicity, but also longevity and security (we are supported by a global reinsurer)
We will allow customers to directly get a quote and apply for life insurance through the website.
We want a very modern look, with our exisiting gold and dark blue colours.
Target Market(s)
30-50 YOs
Industry/Entity Type
Life Insurance
Requirements
Must have
- - Life insurance quick quotation tool.
- Phone number.
- Ability to drill to information on different types of life insurance.
- Positive imagery
- our logo (refer www.brightfern.com.au)
Nice to have
- Target market is 30-40year olds.
Portal for advisers to access
Should not have
- Clip art
Cliched images

```html
<!DOCTYPE html>
<html lang="en">
<head>
<meta charset="utf-8">
<title>BrightFern Life Insurance</title>
<link rel="stylesheet" href="https://fonts.googleapis.com/css2?family=Arimo:wght@400;700&display=swap">
<style>
:root{
  --gold:#e0b623;
  --gold-deep:#c99c10;
  --gold-box:#dfb92a;
  --navy:#2a1a78;
  --navy-dark:#1c0f5c;
  --ink:#222;
  --grey-band:#f1f1f1;
  --grey-mid:#dedede;
  --grey-foot:#c9c9c9;
  --white:#fff;
}
*{box-sizing:border-box;margin:0;padding:0}
html,body{width:1200px;height:1156px;overflow:hidden}
body{position:relative;font-family:"Arimo",Arial,sans-serif;color:var(--ink);background:var(--white)}
.abs{position:absolute}
.top-band{left:0;top:0;width:1200px;height:172px;background:linear-gradient(#ecc73a,var(--gold-deep))}
.content-band{left:0;top:543px;width:1200px;height:309px;background:var(--grey-band)}
.news-band{left:0;top:852px;width:1200px;height:223px;background:var(--grey-mid)}
.footer-band{left:0;top:1075px;width:1200px;height:81px;background:var(--grey-foot)}
.sheet{left:160px;top:12px;width:880px;height:531px;background:linear-gradient(#fafafa,#fff 25%);border-radius:6px 6px 0 0;box-shadow:0 0 12px rgba(0,0,0,.18)}
.sheet-lower{left:160px;top:543px;width:880px;height:309px;background:var(--white)}
.sheet-foot{left:160px;top:1075px;width:880px;height:81px;background:var(--white)}
.brand{left:200px;top:52px;display:flex;align-items:center;gap:12px}
.brand-mark{width:34px;height:34px;border-radius:50%;background:var(--navy)}
.brand-name{font-size:34px;color:var(--navy);font-weight:400;letter-spacing:.5px}
.search{left:716px;top:55px;width:169px;height:28px;border:1px solid #ccc;border-radius:3px;background:#fff;font-size:11px;font-style:italic;padding:7px 8px;color:#333}
.search svg{position:absolute;right:4px;top:3px}
.portal-btn{left:892px;top:54px;width:121px;height:29px;background:var(--navy);color:#fff;font-size:12px;text-align:center;line-height:29px;border-radius:3px}
.social{display:flex;gap:5px}
.social span{width:21px;height:21px;border-radius:3px;display:block}
.s1{background:#3b5998}.s2{background:#45b0e3}.s3{background:#1a6ea8}.s4{background:#f08a18}
.social-top{left:906px;top:92px}
.nav{left:168px;top:125px;width:863px;height:39px;border-radius:20px;background:linear-gradient(#4a3a98,var(--navy) 55%,var(--navy-dark));display:flex;color:#fff;font-size:11.5px;box-shadow:0 2px 3px rgba(0,0,0,.25)}
.nav a{color:#fff;text-decoration:none;display:block;text-align:center;line-height:39px;border-right:1px solid rgba(255,255,255,.2)}
.nav a:last-child{border:none}
.hero-frame{left:168px;top:180px;width:863px;height:340px;background:#fff;border:1px solid #ddd;box-shadow:0 18px 14px -12px rgba(0,0,0,.35)}
.hero-img{left:174px;top:186px;width:852px;height:329px;background:linear-gradient(100deg,#e8e48a 0%,#8fb545 30%,#5c8f2e 60%,#a8c948 80%,#6a9a32 100%)}
.hero-img::after{content:"";position:absolute;left:0;right:0;bottom:0;height:120px;background:linear-gradient(transparent,rgba(240,214,40,.75))}
.hero-caption{left:197px;top:440px;font-size:25px;font-weight:700;color:#111;z-index:2}
.dots{left:572px;top:488px;display:flex;gap:6px;z-index:2}
.dots span{width:15px;height:15px;border-radius:50%;background:#eee;border:2px solid #999}
.dots .on{background:#e22}
.col-head{font-size:12.5px;color:var(--navy);height:30px;border-bottom:3px solid var(--navy);padding-top:12px}
.col{top:568px;width:273px}
.col svg{position:absolute;right:8px;top:0}
.links{list-style:none;margin-top:14px;font-size:12px;line-height:15px}
.links li{position:relative;padding-left:33px;margin-bottom:14px}
.links li::before{content:"";position:absolute;left:19px;top:3px;border-left:8px solid var(--gold);border-top:5px solid transparent;border-bottom:5px solid transparent}
.col-text{font-size:12px;line-height:15px;padding-left:21px;margin-top:14px}
.col-text p{margin-bottom:15px}
.col-text u{color:#333}
.read-btn{width:111px;height:30px;border-radius:15px;background:linear-gradient(#4a3a98,var(--navy-dark));color:#fff;font-size:12px;text-align:center;line-height:30px}
.news{left:168px;top:876px;width:567px;height:171px;background:#fff;border:1px solid #ccc;border-radius:4px}
.news h2{position:absolute;left:67px;top:12px;font-size:15.5px;font-weight:400;color:#333}
.news-item{position:absolute;top:38px;width:192px;font-size:12px;line-height:16px;color:#333}
.arrow-tab{position:absolute;top:72px;width:24px;height:47px;background:linear-gradient(#f4f4f4,#c8c8c8);border:1px solid #aaa}
.cta{left:757px;top:876px;width:274px;height:171px;background:var(--gold-box);color:var(--navy)}
.cta h2{position:absolute;left:13px;top:12px;font-size:15.5px;font-weight:700}
.cta p{position:absolute;left:13px;width:250px;font-size:10px;line-height:12px}
.cta-btn{left:159px;top:135px;width:100px;height:27px;border-radius:13px;background:linear-gradient(#4a3a98,var(--navy-dark));color:#fff;font-size:10.5px;line-height:27px;padding-left:38px}
.cta-btn i{position:absolute;left:6px;top:5px;width:20px;height:17px;background:#6a5bb8;border-radius:3px}
.cta-btn i::after{content:"";position:absolute;left:7px;top:4px;border-left:7px solid #fff;border-top:4.5px solid transparent;border-bottom:4.5px solid transparent}
.foot-links{left:160px;top:1095px;width:880px;text-align:center;font-size:12px;color:var(--navy)}
.foot-links span{margin:0 12px}
.copyright{left:160px;top:1119px;width:880px;text-align:center;font-size:11px;color:#333}
.social-foot{left:912px;top:1104px}
</style>
</head>
<body>
<div class="abs top-band"></div>
<div class="abs content-band"></div>
<div class="abs news-band"></div>
<div class="abs footer-band"></div>
<div class="abs sheet"></div>
<div class="abs sheet-lower"></div>
<div class="abs sheet-foot"></div>

<header>
  <div class="abs brand"><span class="brand-mark"></span><span class="brand-name">BrightFern</span></div>
  <div class="abs search">Search
    <svg width="22" height="22" viewBox="0 0 22 22"><circle cx="9" cy="9" r="6" fill="none" stroke="#111" stroke-width="2.5"/><line x1="13" y1="13" x2="20" y2="19" stroke="#111" stroke-width="3.5" stroke-linecap="round"/></svg>
  </div>
  <div class="abs portal-btn">Adviser Portal</div>
  <div class="abs social social-top"><span class="s1"></span><span class="s2"></span><span class="s3"></span><span class="s4"></span></div>
  <nav class="abs nav">
    <a style="width:141px">HOME</a>
    <a style="width:231px">CHOOSING LIFE INSURANCE</a>
    <a style="width:195px">GET LIFE INSURANCE</a>
    <a style="width:128px">CLAIMS</a>
    <a style="width:168px">ABOUT US</a>
  </nav>
</header>

<section>
  <div class="abs hero-frame"></div>
  <div class="abs hero-img" role="img" aria-label="Woman with open arms in a sunny meadow of yellow wildflowers"></div>
  <div class="abs hero-caption">Lorem Ipsum Dolor Sit Amet</div>
  <div class="abs dots"><span class="on"></span><span></span><span></span></div>
</section>

<section>
  <div class="abs col" style="left:168px">
    <div class="col-head" style="padding-left:16px">Insurance Shortcuts</div>
    <ul class="links">
      <li>Life Insurance</li>
      <li>Total and Permanent<br>Disablement Insurance</li>
      <li>Trauma Insurance</li>
      <li>Income Protection<br>Insurance</li>
      <li>Business Expences<br>Insurance</li>
    </ul>
  </div>
  <div class="abs col" style="left:463px">
    <div class="col-head" style="padding-left:21px">Why Coose Bright Fern</div>
    <svg width="38" height="38" viewBox="0 0 38 38"><circle cx="19" cy="19" r="16.5" fill="#fff" stroke="#2a1a78" stroke-width="3"/><text x="19" y="27" text-anchor="middle" font-family="Arimo,Arial,sans-serif" font-weight="700" font-size="22" fill="#2a1a78">?</text></svg>
    <div class="col-text"><p>BrightFern life limited has more than 130<br>years experiences as one of Australia's<br>leading friendly societies.</p></div>
  </div>
  <div class="abs col" style="left:757px">
    <div class="col-head" style="padding-left:18px">Contact an Advisor</div>
    <svg width="38" height="38" viewBox="0 0 38 38"><circle cx="19" cy="19" r="16.5" fill="#fff" stroke="#2a1a78" stroke-width="3"/><path d="M10 17c0-4 4-6 9-6s9 2 9 6h-4l-1-2h-8l-1 2z" fill="#2a1a78"/><rect x="12" y="19" width="14" height="8" rx="2" fill="#2a1a78"/><circle cx="19" cy="23" r="2" fill="#fff"/></svg>
    <div class="col-text" style="padding-left:18px">
      <p>Questions?</p>
      <p>Do you need help to find<br>an Adviser?</p>
      <p>Call Us now on<br>1300 482917 or<br><u>send us an email today</u></p>
    </div>
  </div>
  <div class="abs read-btn" style="left:600px;top:774px">Read more</div>
  <div class="abs read-btn" style="left:895px;top:774px">Read more</div>
</section>

<section>
  <div class="abs news">
    <h2>Latest News</h2>
    <div class="news-item" style="left:67px">Share over announced BrightFern<br>has announced non-renounceable<br>pro rata offer of shares each at an<br>issue price of $0.50 to eligible<br>Shareholders on the basis of eight<br>shares for every seven shares on<br>15th july 2011</div>
    <div class="news-item" style="left:317px">Share over announced BrightFern<br>has announced non-renounceable<br>pro rata offer of shares each at an<br>issue price of $0.50 to eligible<br>Shareholders on the basis of eight<br>shares for every seven shares on<br>15th july 2011</div>
    <div class="arrow-tab" style="left:15px"><svg width="22" height="45"><path d="M14 16l-7 6.5 7 6.5z" fill="#333"/></svg></div>
    <div class="arrow-tab" style="left:527px"><svg width="22" height="45"><path d="M8 16l7 6.5-7 6.5z" fill="#333"/></svg></div>
  </div>
  <div class="abs cta">
    <h2>Get Life Insurance</h2>
    <p style="top:44px">It is an important moment when you appreciate the value of the things in your life that really matter.</p>
    <p style="top:80px">Now that you have decided to get life insurance, BrightFern makes the process simple and straight forward.</p>
    <div class="abs cta-btn"><i></i>Read more</div>
  </div>
</section>

<footer>
  <div class="abs foot-links">BrightFerns Home<span>I</span>Terms Of Use<span>I</span>Privacy Policy</div>
  <div class="abs copyright">Copyright © 2012. BrightFernn.com. All rights reserved</div>
  <div class="abs social social-foot"><span class="s1"></span><span class="s2"></span><span class="s3"></span><span class="s4"></span></div>
</footer>
</body>
</html>
```